Up to the Challenge? Canadian based consulting company needs a two sided business card design

A Canadian based security risk management consulting company needs a two-sided business card design. What we do is provide advice and guidance related to emergency, security and business continuity management for small, medium and large companies to help ensure the protection of their people, assets, information, services, operations and reputation.

The final design should be simple, only one or two colours, eye catching, professional and one that makes people look at three or more times just because it looks so darn good.

I have include examples of business cards I like.

Target Market(s)

Small, medium and large companies.

Industry/Entity Type

Security

Contact Information for Business Card

Business Card Size: Standard size of 3.5" (89mm) x 2.0" (51mm) - (see full specifications and guides on PRINTA's website if required)
Card Stock: Looking to use PRINTA's Velda 32pt stock textured paper - seam colour either chili red or black
Business Name: The Harrowfield Group
Website: www.theharrowfieldgroup.example
Telephone: (555)214-0397
Name: Dana Forsythe
Position: Principle
e-mail: Dana.Forsythe@theharrowfieldgroup.example

Font styles to use
Serif

Colors
ec1f27
000000
9d9d9d
aaaaaa
606060

Requirements
Must have
• - "The Harrowfield Group" logo (see uploaded files). I have included grey scale and colour versions.
• - Business card details (as above)
Nice to have
• - One side black or grey scale.
• - Other side would likely be white.
• - Everyone likes the silver logo on the black background.
• - Small element of colour i.e. red but I'm leaning more to greyscale.
Should not have
• - A lot of colour. Keep it simple.

```html
<!DOCTYPE html>
<html lang="en">
<head>
<meta charset="utf-8">
<title>The Harrowfield Group – Business Card</title>
<link rel="stylesheet" href="https://fonts.googleapis.com/css2?family=Montserrat:wght@400;600;700&display=swap">
<style>
  :root {
    --stage: #1c1c1c;
    --card-black: #111111;
    --card-white: #ffffff;
    --brand-red: #ec1f27;
    --silver: #9d9d9d;
    --ink: #303030;
    --ink-soft: #606060;
  }
  * { margin: 0; padding: 0; box-sizing: border-box; }
  html, body {
    width: 1200px; height: 815px; overflow: hidden;
    background: var(--stage);
    font-family: "Montserrat", Arial, sans-serif;
  }
  .canvas {
    position: relative; width: 1200px; height: 815px;
    display: flex; align-items: center; justify-content: center; gap: 60px;
  }
  .card {
    position: relative; width: 520px; height: 297px;
    box-shadow: 0 18px 40px rgba(0,0,0,.55);
  }
  .card--front {
    background: var(--card-black);
    display: flex; align-items: center; justify-content: center;
  }
  .brand-name {
    font-weight: 600; color: var(--silver);
    text-transform: uppercase; letter-spacing: 3px;
  }
  .card--front .brand-name { font-size: 26px; }
  .card--back { background: var(--card-white); }
  .back-brand {
    position: absolute; top: 34px; right: 34px;
    display: flex; align-items: center; gap: 10px;
  }
  .back-brand .mark {
    width: 44px; height: 44px; background: var(--brand-red);
  }
  .back-brand .brand-name { font-size: 11px; letter-spacing: 1.5px; color: var(--ink-soft); }
  .contact {
    position: absolute; left: 34px; bottom: 36px;
  }
  .contact__name {
    font-weight: 700; font-size: 19px; color: var(--ink);
    text-transform: uppercase; letter-spacing: .5px;
  }
  .contact__role {
    font-weight: 700; font-size: 13px; color: var(--brand-red); margin-bottom: 8px;
  }
  .contact__lines {
    border-left: 3px solid var(--brand-red);
    padding-left: 10px;
    font-size: 11px; line-height: 1.5; color: var(--ink-soft);
    list-style: none;
  }
</style>
</head>
<body>
  <main class="canvas">
    <section class="card card--front" aria-label="Card front">
      <span class="brand-name">The Harrowfield Group</span>
    </section>

    <section class="card card--back" aria-label="Card back">
      <div class="back-brand">
        <span class="mark"></span>
        <span class="brand-name">The Harrowfield Group</span>
      </div>
      <div class="contact">
        <p class="contact__name">Dana Forsythe</p>
        <p class="contact__role">Principle</p>
        <ul class="contact__lines">
          <li>(555)214-0397</li>
          <li>Dana.Forsythe@theharrowfieldgroup.example</li>
          <li>ca.profilelink.example/in/danaforsythe</li>
          <li>www.theharrowfieldgroup.example</li>
        </ul>
      </div>
    </section>
  </main>
</body>
</html>
```